Need a Middle Eastern/Cooking/Nutrition Design please :)

Hi I am looking to revamp my Middle Eastern/Cooking/Nutrition Blog for something that is clean, sophisticated yet sultry. My site now www.plumhavenkitchen.com is messy and needs more color help with background. Please send anything you think is suitable for the concept.
Target Market(s)
high end
Industry/Entity Type
Nutrition
Requirements
Must have
- Your work looks wonderful!
I am looking forward to your designs! I am really trying to revamp my current site www.plumhavenkitchen.com to be more clean and sophisticated.
I like this color palette or maybe royal purple and gold. http://www.hueweavers.net/palette/418205/Amber_Dunes
I had my website evaluated by a brand specialist and this what she said I should be doing :) Let me know what you think- really appreciate it!
Comments Below:
Given your brand identity, I think you want to go for something clean and simple but with touches of bold color and iconography. You want the site to come off as approachable, but to also have an exotic and slightly mysterious edge. Perhaps choose a solid background color and use stylish icons, flourishes and images to bring the Middle Eastern/Mediterranean flavor.
I also recommend that you use a neutral color or a whitewashed design as your background. It is easier on the eyes to read a lot of text when it’s a neutral (light or white) background color with a darker font.
Here is a color palette that I like for you: http://www.hueweavers.net/palette/418205/Amber_Dunes
In terms of organization, I think it would be great to have your home page be a jump page. So, rather than having a list of your recent posts, perhaps you can welcome guests with a picture of yourself/your food/your brand.
Then, you could have a menu of options for people to explore your site (kind of like the bar you have at the top of your page now). But instead of just having the text, you could use images as the links to the different pages. This would include a link to classes, recipes, nutritional information, products, TV shows/videos, bio, etc. And you could organize it in a creative way on the page.
There are so many ways that you can organize your site, and it’s completely up to you! But here are some examples that I think you could look to for inspiration:
http://marisolvantrecca.com/
http://www.willowbrookhostess.com/
http://www.dunavelm.com/
http://www.trylentilo.com/trylentilo.com/Lentilo.html
http://www.korvidash.com/
http://www.bresklunch.com/
For your brand name, ultimately, you want something that reflects the down to earth yet somewhat exotic nature of your brand. The actual brand name is up to you…but I do like where you’re going with the ingredients.
I want simple and sophisticated yet also portrays the mysterious and exotic Middle East. The site colors and pictures should transport people but also want it clean. I think my site is too busy now.
The content and layout could be the same but the logo, domain name possible and website name, background and color scheme all have to change although I do like dark purple and gold as possibilities along with the color pattern I sent already,
Im not sure if its a single page or full project but I do want a total revamp of the scheme- do you need to redo the website or just remake the existing because I can provide the website info if thats the case . I can pay the up front cost now. I believe the quote is 300.
Also im not sure if I should stick with the Sprig up name or here are other name options if you think they meet the sophisticated brand of the Middle East more.
tahini & honey
fig & chickpea
saffron & rosewater- very exotic
harissa & honey
pomegranates & pistachios
saffron & pomegranates
figs & saffron
The name should be playful and fun for the site. I like the idea of ingredients because it brings both the Mediterranean and Middle East imagery and allows for broad appeal.
Thank you soooooooooo much- I know it’s a lot to think about and I greatly appreciate your insight and talents in this!!
Nice to have
- Clean, sophisticated, sultry, exotic and professional
Should not have
- too busy

```html
<!DOCTYPE html>
<html lang="en">
<head>
<meta charset="utf-8">
<title>Sprig up – Taste of the Mediterranean and Middle East</title>
<link href="https://fonts.googleapis.com/css2?family=Arimo:wght@400;700&display=swap" rel="stylesheet">
<style>
:root{
  --page-bg:#3a0d3d;
  --page-deep:#2c0930;
  --column-bg:#44104a;
  --panel:#5a1a5f;
  --panel-edge:#7d3d82;
  --gold:#e3b94f;
  --gold-deep:#c99a2c;
  --gold-light:#f0d27a;
  --ink-dark:#3c0c40;
  --text-light:#f3e7f2;
  --text-muted:#d9b9d8;
}
*{box-sizing:border-box;margin:0;padding:0}
html,body{width:1200px;height:2225px;overflow:hidden}
body{
  position:relative;
  background:radial-gradient(ellipse at 50% 30%,#4a1450 0%,var(--page-bg) 55%,var(--page-deep) 100%);
  font-family:"Arimo",Arial,sans-serif;
  color:var(--text-light);
}
.column{
  position:absolute;left:54px;top:0;width:1092px;height:2167px;
  background:linear-gradient(180deg,#4a1350,var(--column-bg) 40%,#3f0e45);
  border-left:2px solid #5e2563;border-right:2px solid #5e2563;
}
.brand{
  position:absolute;left:0;top:26px;width:1200px;text-align:center;
  font-weight:700;font-size:66px;letter-spacing:10px;color:var(--gold);text-transform:uppercase;
}
.tagline{
  position:absolute;left:0;top:112px;width:1200px;text-align:center;
  font-weight:700;font-size:18px;color:#fff;letter-spacing:.5px;
}
.main-nav{
  position:absolute;left:77px;top:154px;width:1046px;height:48px;
  background:linear-gradient(180deg,#6a2670,#531a58);
  border:2px solid var(--panel-edge);
  display:flex;align-items:center;
}
.main-nav a{
  color:var(--gold);text-decoration:none;font-size:16px;text-transform:uppercase;
  position:absolute;top:13px;
}
.hero{
  position:absolute;left:93px;top:229px;width:1014px;height:391px;
  background:var(--panel);border:2px solid var(--panel-edge);
}
.hero .photo{
  position:absolute;left:14px;top:14px;width:984px;height:361px;
  background:linear-gradient(100deg,#f4f1ee 0%,#e8ddd8 18%,#c8432c 35%,#d95a34 55%,#b8341f 72%,#6a8a3a 88%,#c9b9a4 100%);
}
.intro{
  position:absolute;left:116px;top:680px;width:690px;
  font-size:14.5px;line-height:25px;color:#fff;
}
.read-more{
  font-size:10px;font-weight:700;letter-spacing:1.5px;color:var(--gold);text-transform:uppercase;
}
.intro .read-more{position:absolute;right:0;top:97px}
.portrait{
  position:absolute;left:826px;top:644px;width:281px;height:170px;
  background:var(--panel);border:2px solid var(--panel-edge);
}
.portrait .photo{
  position:absolute;left:11px;top:11px;width:255px;height:145px;
  background:linear-gradient(90deg,#2c4fb0,#6b86d8 40%,#c9a58c 55%,#4b66c4 80%,#2a45a0);
}
.divider{
  position:absolute;left:98px;top:830px;width:1009px;border-top:2px dotted #7a4a7e;
}
.post{
  position:absolute;left:93px;width:703px;height:356px;
  background:var(--panel);border:2px solid var(--panel-edge);
}
.post h2{
  position:absolute;left:20px;top:16px;font-weight:400;font-size:27px;color:var(--gold);
}
.post .meta{
  position:absolute;left:16px;top:60px;width:668px;height:34px;
  background:linear-gradient(180deg,var(--gold-light),var(--gold));
  color:var(--ink-dark);font-size:13px;line-height:34px;padding-left:6px;
}
.post .meta .comments{position:absolute;right:18px;top:0}
.post .meta svg{position:absolute;right:110px;top:8px}
.post .thumb{
  position:absolute;left:19px;top:116px;width:222px;height:168px;
  background:linear-gradient(110deg,#f2eeea 0%,#d2492f 35%,#c73a24 60%,#5f8a36 85%,#efe7df 100%);
}
.post p{
  position:absolute;left:258px;top:112px;width:426px;font-size:13.6px;line-height:28.5px;color:var(--text-light);
}
.post .rule{position:absolute;left:16px;top:312px;width:668px;border-top:1px solid #7d4a82}
.post .share{
  position:absolute;left:20px;top:322px;font-size:13px;color:var(--gold);display:flex;align-items:center;gap:10px;
}
.share .icon{width:22px;height:22px;background:var(--gold);border-radius:4px}
.post .read-more{position:absolute;right:20px;top:330px}
.widget{
  position:absolute;left:819px;width:290px;background:var(--panel);border:2px solid var(--panel-edge);
}
.widget h3{font-size:17px;font-weight:400;text-align:center;line-height:22px}
.widget .band{
  background:linear-gradient(180deg,var(--gold-light),var(--gold));color:var(--ink-dark);padding:7px 10px;
}
.widget .photo{
  position:absolute;left:14px;width:258px;height:110px;
  background:linear-gradient(110deg,#f2eeea 0%,#d2492f 35%,#c73a24 60%,#5f8a36 85%,#efe7df 100%);
}
.widget p{position:absolute;left:22px;width:250px;font-size:12.5px;line-height:20px;color:#fff}
.more-btn{
  position:absolute;right:16px;width:76px;height:22px;background:linear-gradient(180deg,var(--gold-light),var(--gold));
  color:var(--ink-dark);font-size:10px;font-weight:700;line-height:22px;text-align:center;letter-spacing:1px;
}
.mailing{
  top:864px;height:141px;background:linear-gradient(180deg,var(--gold-light),var(--gold-deep));border-color:#b88a2a;
}
.mailing h3{position:absolute;left:18px;top:10px;color:var(--ink-dark);font-weight:700;text-align:left;font-size:17px}
.mailing .field{
  position:absolute;left:16px;top:40px;width:255px;height:38px;background:var(--ink-dark);border-radius:3px;
}
.mailing .field svg{position:absolute;right:10px;top:9px}
.mailing .social{position:absolute;left:62px;top:89px;display:flex;gap:24px}
.mailing .social span{width:40px;height:40px;background:var(--ink-dark);border-radius:5px}
.pager{position:absolute;top:2053px;height:32px;font-size:15px;line-height:30px;text-align:center;
  border:1px solid #6a2c70;background:#4a1350;color:#9a5aa0}
.pager.current{background:var(--gold);color:var(--ink-dark);border-color:var(--gold)}
.footer-line{position:absolute;left:16px;top:2166px;width:1168px;border-top:1px solid #5e2563}
.copyright{position:absolute;left:0;top:2182px;width:1200px;text-align:center;font-size:12px;color:var(--gold)}
</style>
</head>
<body>
<div class="column"></div>

<header>
  <div class="brand">Sprig up</div>
  <div class="tagline">TASTE OF THE MEDITERRANEAN AND MIDDLE EAST</div>
  <nav class="main-nav">
    <a href="#" style="left:16px">Home</a>
    <a href="#" style="left:104px">Why Mediterranean &amp; Mideast Cuisine?</a>
    <a href="#" style="left:492px">Cooking Class</a>
    <a href="#" style="left:670px">Healthy Recipes</a>
    <a href="#" style="left:854px">About</a>
    <a href="#" style="left:945px">Contact</a>
  </nav>
</header>

<section class="hero"><div class="photo" role="img" aria-label="Close-up of roasted stuffed tomato with herbs and sauce"></div></section>

<section>
  <div class="intro">
    This website is about me sharing how to be fit and full Mediterranean style by sharing healthy Mediterranean recipes and inspiring others with the wise Mediterranean lifestyle motto to: savor food and savor life! I got inspired to do this website by my family- and I mean everyone in it (including the semi-annoying members).
    <span class="read-more">[ Read more ]</span>
  </div>
  <div class="portrait"><div class="photo" role="img" aria-label="Portrait of the blog author by the sea"></div></div>
</section>

<div class="divider"></div>

<main>
  <article class="post" style="top:864px">
    <h2>Fall Butternut Squash with Homemade Harissa</h2>
    <div class="meta">Posted on October 11, 2011 in: Healthy Recipes
      <svg width="20" height="18" viewBox="0 0 20 18"><ellipse cx="8" cy="7" rx="8" ry="6" fill="#3c0c40"/><path d="M3 11 L2 17 L8 12Z" fill="#3c0c40"/><ellipse cx="14" cy="11" rx="6" ry="5" fill="#5a1a5f"/></svg>
      <span class="comments">0 comments</span></div>
    <div class="thumb" role="img" aria-label="Roasted butternut squash with harissa"></div>
    <p>When its fall, I love buying squash from the market and feeling like I am all ready for the new season even though I have no idea what I am going to be doing with the squash right then and there. But this recipe is my go to for a decadent feast of butternut squash and being so tasty, its a great way to embark on an amazing fall. I love butternut squash particularly roasted because you get the natural caramelization from the natural sugars in the squash to come out.</p>
    <div class="rule"></div>
    <div class="share">Share it: <span class="icon"></span><span class="icon"></span></div>
    <span class="read-more">[ Read more ]</span>
  </article>

  <article class="post" style="top:1246px">
    <h2>Fall Butternut Squash with Homemade Harissa</h2>
    <div class="meta">Posted on October 11, 2011 in: Healthy Recipes
      <svg width="20" height="18" viewBox="0 0 20 18"><ellipse cx="8" cy="7" rx="8" ry="6" fill="#3c0c40"/><path d="M3 11 L2 17 L8 12Z" fill="#3c0c40"/><ellipse cx="14" cy="11" rx="6" ry="5" fill="#5a1a5f"/></svg>
      <span class="comments">0 comments</span></div>
    <div class="thumb" role="img" aria-label="Roasted butternut squash with harissa"></div>
    <p>When its fall, I love buying squash from the market and feeling like I am all ready for the new season even though I have no idea what I am going to be doing with the squash right then and there. But this recipe is my go to for a decadent feast of butternut squash and being so tasty, its a great way to embark on an amazing fall. I love butternut squash particularly roasted because you get the natural caramelization from the natural sugars in the squash to come out.</p>
    <div class="rule"></div>
    <div class="share">Share it: <span class="icon"></span><span class="icon"></span></div>
    <span class="read-more">[ Read more ]</span>
  </article>

  <article class="post" style="top:1629px">
    <h2>Fall Butternut Squash with Homemade Harissa</h2>
    <div class="meta">Posted on October 11, 2011 in: Healthy Recipes
      <svg width="20" height="18" viewBox="0 0 20 18"><ellipse cx="8" cy="7" rx="8" ry="6" fill="#3c0c40"/><path d="M3 11 L2 17 L8 12Z" fill="#3c0c40"/><ellipse cx="14" cy="11" rx="6" ry="5" fill="#5a1a5f"/></svg>
      <span class="comments">0 comments</span></div>
    <div class="thumb" role="img" aria-label="Roasted butternut squash with harissa"></div>
    <p>When its fall, I love buying squash from the market and feeling like I am all ready for the new season even though I have no idea what I am going to be doing with the squash right then and there. But this recipe is my go to for a decadent feast of butternut squash and being so tasty, its a great way to embark on an amazing fall. I love butternut squash particularly roasted because you get the natural caramelization from the natural sugars in the squash to come out.</p>
    <div class="rule"></div>
    <div class="share">Share it: <span class="icon"></span><span class="icon"></span></div>
    <span class="read-more">[ Read more ]</span>
  </article>
</main>

<aside>
  <div class="widget mailing">
    <h3>Subscribe to our mailing list</h3>
    <div class="field"><svg width="22" height="20" viewBox="0 0 22 20"><path d="M5 2 L17 10 L5 18 L9 10Z" fill="#e3b94f"/></svg></div>
    <div class="social"><span></span><span></span><span></span></div>
  </div>

  <div class="widget" style="top:1032px;height:297px">
    <h3 style="color:var(--gold);padding-top:12px">Suggestion and Question Box</h3>
    <div class="photo" style="top:56px" role="img" aria-label="Plated roasted vegetable dish"></div>
    <p style="top:178px">If you have a suggestion for a recipe or any questions, we would be glad to hear it! Just write it in the box and hit submit :)</p>
    <div class="more-btn" style="top:262px">MORE &gt;&gt;</div>
  </div>

  <div class="widget" style="top:1354px;height:309px">
    <h3 class="band">Benefits of Middle Eastern &amp; Mediterranean Cuisine</h3>
    <div class="photo" style="top:74px" role="img" aria-label="Plated roasted vegetable dish"></div>
    <p style="top:196px">There really is a delicious way to be fit, full and healthy! Much research and studies have been done on the benefits of the Mediterranean cuisine.</p>
    <div class="more-btn" style="top:274px">MORE &gt;&gt;</div>
  </div>

  <div class="widget" style="top:1692px;height:312px">
    <h3 class="band">Selma's Cedar Table Gourmet Products in Stores</h3>
    <div class="photo" style="top:76px;background:linear-gradient(90deg,#b06cc0,#e8d9ea 15%,#c4a77a 50%,#e8d9ea 85%,#b06cc0)" role="img" aria-label="Packaged baklava product"></div>
    <p style="top:198px">There really is a delicious way to be fit, full and healthy! Much research and studies have been done on the benefits of the Mediterranean cuisine.</p>
    <div class="more-btn" style="top:276px">MORE &gt;&gt;</div>
  </div>
</aside>

<nav aria-label="Pages">
  <span class="pager" style="left:245px;width:82px">Previous</span>
  <span class="pager current" style="left:347px;width:33px">1</span>
  <span class="pager" style="left:397px;width:33px">2</span>
  <span class="pager" style="left:443px;width:33px">3</span>
  <span class="pager" style="left:493px;width:33px">4</span>
  <span class="pager" style="left:541px;width:33px">5</span>
  <span class="pager" style="left:597px;width:75px">Next</span>
</nav>

<footer>
  <div class="footer-line"></div>
  <div class="copyright">Copyright © 2012 Sprig up</div>
</footer>
</body>
</html>
```